Chorkonzert Thema Die KlangKiesel fällt aus dem Rahmen
Zielgruppe
Wir sind ein A-Capella Chor 'KlangKiesel'. Wir wollen Jung und Alt ansprechen.
Es sollen Plakate (30x42 cm) und Handzettel erstellt werden.
Aufgabenstellung
Wir sind noch völlig offen. Beim letzten Konzert wurde ein Foto (mit allen verwendet)
Entweder könnte wieder ein Foto mitverarbeitet werden. Wir laden mal zwei drei Fotos hoch. Von den Einzelstimmen sind jeweils Bilder noch vorhanden. Würden aber auch spezielle Fotos machen lassen je nachdem.
Gerne ein Plakat das entsprechend dem Konzerttitel etwas aus dem Rahmen fällt.
Text:
Wann: 10. und 12.03.2017 um ? Uhr
Eintritt: 8 Euro VVK 10 Euro AK
Kartenbestellung

```html
<!DOCTYPE html>
<html lang="de">
<head>
<meta charset="utf-8">
<title>KlangKiesel – Chorkonzert</title>
<link rel="stylesheet" href="https://fonts.googleapis.com/css2?family=Mulish:wght@400;600;800;900&display=swap">
<style>
  :root {
    --wall-light: #d9d8cf;
    --wall-dark: #a9a89f;
    --floor-light: #8a5a45;
    --floor-dark: #4e2c20;
    --frame-light: #efefef;
    --frame-dark: #9c9c9c;
    --board-edge: #1c1c1c;
    --green: #6ccf3a;
    --green-deep: #3f8a2a;
    --white: #ffffff;
  }
  html, body {
    margin: 0;
    padding: 0;
    width: 917px;
    height: 1200px;
    overflow: hidden;
  }
  .poster {
    position: relative;
    width: 917px;
    height: 1200px;
    overflow: hidden;
    background: radial-gradient(ellipse at 50% 40%, var(--wall-light), var(--wall-dark));
    font-family: "Mulish", sans-serif;
  }
  .floor {
    position: absolute;
    left: 0; top: 916px;
    width: 917px; height: 284px;
    background: linear-gradient(180deg, var(--floor-light), var(--floor-dark));
  }
  .stage { position: absolute; inset: 0; }
  .choir-photo {
    position: absolute;
    left: 44px; top: 72px;
    width: 652px; height: 320px;
    clip-path: polygon(0px 168px, 206px 88px, 376px 58px, 516px 0px, 652px 0px, 652px 143px, 476px 196px, 256px 248px, 0px 320px);
    background: linear-gradient(160deg, #7fd85a, var(--green-deep));
  }
  .helpers-photo {
    position: absolute;
    left: 512px; top: 684px;
    width: 248px; height: 492px;
    clip-path: polygon(0% 17%, 40% 6%, 72% 0%, 100% 12%, 95% 100%, 5% 100%);
    background: linear-gradient(180deg, #9ad98a 0%, #3d6b34 45%, #3e4652 75%, #2d323a 100%);
  }
  .copy {
    position: absolute;
    inset: 0;
    color: var(--white);
  }
  .line {
    position: absolute;
    margin: 0;
    line-height: 1;
    white-space: nowrap;
    transform-origin: 0 85%;
  }
  .kicker {
    left: 300px; top: 340px;
    font-size: 27px; font-weight: 600;
    transform: rotate(-15deg);
  }
  .title {
    left: 156px; top: 410px;
    transform: rotate(-12deg);
  }
  .title .die {
    font-size: 30px; font-weight: 800; color: var(--green);
    margin-right: 8px;
  }
  .title .name {
    font-size: 62px; font-weight: 900;
    text-shadow: 0 0 14px rgba(255,255,255,.35), 0 3px 4px rgba(0,0,0,.6);
  }
  .subtitle {
    left: 180px; top: 525px;
    font-size: 32px; font-weight: 600;
    transform: rotate(-13deg);
  }
  .fact {
    font-size: 24px; font-weight: 800;
    transform: rotate(-13.5deg);
  }
  .fact .label { color: var(--green); }
  .fact-when { left: 196px; top: 608px; }
  .fact-where { left: 212px; top: 644px; }
  .fact-price { left: 228px; top: 684px; }
  .fact-order { left: 232px; top: 736px; }
  .fact-mail { left: 240px; top: 784px; }
</style>
</head>
<body>
<main class="poster">
  <div class="floor" role="img" aria-label="Holzdielenboden"></div>

  <svg class="stage" width="917" height="1200" viewBox="0 0 917 1200" aria-hidden="true">
    <defs>
      <linearGradient id="frameShade" x1="0" y1="0" x2="1" y2="1">
        <stop offset="0" stop-color="var(--frame-light)"/>
        <stop offset="1" stop-color="var(--frame-dark)"/>
      </linearGradient>
      <radialGradient id="boardShade" cx="0.6" cy="0.45" r="0.7">
        <stop offset="0" stop-color="#3a3a3a"/>
        <stop offset="1" stop-color="var(--board-edge)"/>
      </radialGradient>
    </defs>
    <rect x="116" y="104" width="704" height="900" fill="url(#frameShade)" rx="2"/>
    <rect x="180" y="160" width="576" height="788" fill="none" stroke="#bdbdbd" stroke-width="6"/>
    <rect x="200" y="180" width="544" height="756" fill="#3c3c3c"/>
    <path d="M0,410 L30,400 C110,620 170,790 214,935 L196,935 C150,800 90,620 0,410 Z" fill="rgba(0,0,0,.25)"/>
    <path d="M20,368 L720,188 L744,188 L744,936 L212,936 C176,800 120,620 20,368 Z" fill="url(#boardShade)"/>
    <path d="M316,382 L520,328" stroke="var(--green)" stroke-width="3" stroke-linecap="round"/>
    <path d="M200,564 L664,456" stroke="var(--green)" stroke-width="3" stroke-linecap="round"/>
  </svg>

  <div class="choir-photo" role="img" aria-label="Foto der Chormitglieder in grünen Hemden, die sich über den oberen Rand des Rahmens lehnen"></div>
  <div class="helpers-photo" role="img" aria-label="Foto zweier Sänger, die den herausfallenden Bildinhalt mit erhobenen Armen stützen"></div>

  <div class="copy">
    <p class="line kicker">Chorkonzert</p>
    <h1 class="line title"><span class="die">Die</span><span class="name">KlangKiesel</span></h1>
    <p class="line subtitle">fällt aus dem Rahmen...</p>
    <p class="line fact fact-when"><span class="label">Wann:</span> 10. und 12.03.2017 um ? Uhr</p>
    <p class="line fact fact-where"><span class="label">Wo:</span> Aula Lindenhofgymnasium</p>
    <p class="line fact fact-price"><span class="label">Eintritt:</span> 8 Euro VVK 10 Euro AK</p>
    <p class="line fact fact-order"><span class="label">Kartenbestellung</span> 07542 - 61870</p>
    <p class="line fact fact-mail">odile.wa@mailpost.de</p>
  </div>
</main>
</body>
</html>
```